Fieldstone Sporting
F.S.S. Sports
Project: Fieldstone Sporting
Fieldstone Sporting - Sports
Creative Brief
Use same font as used in my logo
Use your better judgement
Professional
Weston L. Barrow Jr.
CEO
Harlow Vale, QX
W.barrow17@quillmail.example
www.FSSsports.example
Logo and web address
Concepts
Business card and stationary design. We provide umpires & referees for teams/organizations.

```html
<!DOCTYPE html>
<html lang="en">
<head>
<meta charset="utf-8">
<title>Fieldstone Sporting Stationery</title>
<link href="https://fonts.googleapis.com/css2?family=Roboto:wght@400;700;900&display=swap" rel="stylesheet">
<style>
  :root {
    --backdrop: #a7a8aa;
    --paper: #ffffff;
    --navy: #46548f;
    --green: #7fc241;
    --ink: #2b2b2b;
    --brand: #2e4a8c;
  }
  * { margin: 0; padding: 0; box-sizing: border-box; }
  html, body { width: 1200px; height: 625px; overflow: hidden; }
  body {
    position: relative;
    background: var(--backdrop);
    font-family: "Roboto", Arial, sans-serif;
    color: var(--ink);
  }
  .piece {
    position: absolute;
    background: var(--paper);
    overflow: hidden;
    box-shadow: 0 1px 2px rgba(0,0,0,0.25);
  }
  .piece svg.art { position: absolute; inset: 0; width: 100%; height: 100%; }
  .logo {
    position: absolute;
    display: flex;
    align-items: center;
    gap: 5px;
    font-weight: 900;
    color: var(--brand);
    white-space: nowrap;
    letter-spacing: 0.01em;
  }
  .logo .mark {
    border-radius: 50%;
    background: var(--green);
    flex: none;
  }
  .contact {
    position: absolute;
    font-size: 5px;
    line-height: 1.45;
    color: var(--ink);
    white-space: nowrap;
  }
  .contact .web { font-weight: 700; }

  .card-front { left: 34px; top: 329px; width: 158px; height: 60px; }
  .card-front .logo { left: 0; right: 0; justify-content: center; top: 19px; font-size: 11px; }
  .card-front .logo .mark { width: 9px; height: 9px; }
  .card-front .contact { left: 0; right: 0; top: 43px; text-align: center; font-size: 4.5px; }

  .card-back { left: 34px; top: 403px; width: 158px; height: 67px; }
  .card-back .contact { left: 8px; top: 21px; font-size: 4px; }
  .card-back .holder { position: absolute; left: 72px; top: 21px; font-size: 4.2px; line-height: 1.4; white-space: nowrap; }
  .card-back .holder .name { font-weight: 700; }

  .letterhead { left: 233px; top: 31px; width: 410px; height: 574px; }
  .letterhead .logo { left: 19px; top: 36px; font-size: 14px; }
  .letterhead .logo .mark { width: 11px; height: 11px; }
  .letterhead .contact { left: 19px; top: 490px; font-size: 5.5px; }

  .envelope-back { left: 679px; top: 82px; width: 483px; height: 218px; }

  .envelope-front { left: 679px; top: 336px; width: 483px; height: 254px; }
  .envelope-front .logo { left: 30px; top: 40px; font-size: 15px; }
  .envelope-front .logo .mark { width: 12px; height: 12px; }
  .envelope-front .contact { left: 92px; top: 82px; font-size: 5.5px; }
</style>
</head>
<body>

  <section class="piece card-front">
    <div class="logo"><span class="mark"></span>Fieldstone Sporting</div>
    <p class="contact"><span class="web">www.FSSsports.example</span></p>
  </section>

  <section class="piece card-back">
    <svg class="art" viewBox="0 0 158 67" preserveAspectRatio="none" aria-hidden="true">
      <path d="M132 0 H158 V67 H88 C115 55 128 32 132 0 Z" fill="var(--navy)"/>
      <path d="M70 67 C100 58 118 40 124 12 C122 40 108 58 84 67 Z" fill="var(--green)"/>
    </svg>
    <p class="contact">
      <span class="web">www.FSSsports.example</span><br>
      Harlow Vale, QX<br>
      Phone: 555-0142<br>
      Fax: 555-0143<br>
      W.barrow17@quillmail.example
    </p>
    <p class="holder"><span class="name">Weston L. Barrow Jr.</span><br>CEO</p>
  </section>

  <section class="piece letterhead">
    <svg class="art" viewBox="0 0 410 574" preserveAspectRatio="none" aria-hidden="true">
      <path d="M356 0 H410 V574 H250 C340 500 370 330 356 0 Z" fill="var(--navy)"/>
      <path d="M170 574 C270 510 325 420 342 250 C340 420 300 510 222 574 Z" fill="var(--green)"/>
    </svg>
    <div class="logo"><span class="mark"></span>Fieldstone Sporting</div>
    <p class="contact">
      <span class="web">www.FSSsports.example</span><br>
      Harlow Vale, QX<br>
      Phone: 555-0142<br>
      Fax: 555-0143<br>
      Email: W.barrow17@quillmail.example
    </p>
  </section>

  <section class="piece envelope-back">
    <svg class="art" viewBox="0 0 483 218" preserveAspectRatio="none" aria-hidden="true">
      <path d="M0 0 H483 V78 C420 100 320 122 241 130 C160 122 60 100 0 78 Z" fill="var(--navy)"/>
    </svg>
  </section>

  <section class="piece envelope-front">
    <svg class="art" viewBox="0 0 483 254" preserveAspectRatio="none" aria-hidden="true">
      <path d="M440 0 H483 V254 H330 C400 215 438 140 440 0 Z" fill="var(--navy)"/>
      <path d="M290 254 C360 220 408 160 420 70 C420 160 380 222 322 254 Z" fill="var(--green)"/>
    </svg>
    <div class="logo"><span class="mark"></span>Fieldstone Sporting</div>
    <p class="contact">
      <span class="web">www.FSSsports.example</span><br>
      Harlow Vale, QX<br>
      Phone: 555-0142<br>
      Fax: 555-0143<br>
      Email: W.barrow17@quillmail.example
    </p>
  </section>

</body>
</html>
```